Redesign Event Flyer for Speaker

We are re-designing our professional event flyer template with new headshot and cleaner, up-to-date design. All design details are in PDF file attached. Thank you for participating :)

Font styles to use
Sans Serif

Colors
3276b5
0355a3

Requirements
Must have
• All elements in PDF file.
Nice to have
Should not have
• Tacky or childish elements.

```html
<!DOCTYPE html>
<html lang="en">
<head>
<meta charset="utf-8">
<title>The Greatest Sale – Event Flyer</title>
<link rel="stylesheet" href="https://fonts.googleapis.com/css2?family=Bebas+Neue&family=Cormorant+SC:wght@600&family=Oswald:wght@300&family=Questrial&family=Ubuntu:wght@400;500&display=swap">
<style>
:root{
  --backdrop:#403838;
  --navy-deep:#142d66;
  --navy-soft:#4b5b91;
  --band-navy:#0d2e62;
  --brand-blue:#0355a3;
  --accent-blue:#3276b5;
  --date-blue:#1d5cb2;
  --silver:#bfc3c9;
  --slate:#5a5a5c;
  --white:#ffffff;
}
*{margin:0;padding:0;box-sizing:border-box}
html,body{width:1200px;height:908px;overflow:hidden;background:var(--backdrop)}
.flyer{
  position:absolute;left:98px;top:123px;width:1006px;height:670px;overflow:hidden;
  background:linear-gradient(100deg,var(--navy-deep) 0%,#1e3a78 45%,var(--navy-soft) 100%);
  box-shadow:0 4px 14px rgba(0,0,0,.45);
  color:var(--white);
}
.flyer-shapes,.speaker-photo{position:absolute;inset:0}
.speaker-name{
  position:absolute;left:428px;top:66px;
  font-family:"Cormorant SC",serif;font-weight:600;font-size:44px;letter-spacing:.5px;white-space:nowrap;
}
.event-title{
  position:absolute;left:428px;top:138px;
  font-family:"Bebas Neue",sans-serif;font-weight:400;font-size:62px;line-height:1;white-space:nowrap;
}
.event-title .highlight{color:var(--date-blue)}
.event-venue{
  position:absolute;left:428px;top:199px;
  font-family:"Oswald",sans-serif;font-weight:300;font-size:27px;line-height:1;white-space:nowrap;
}
.event-date{
  position:absolute;left:428px;top:260px;width:361px;height:34px;
  background:var(--date-blue);
  font-family:"Ubuntu",sans-serif;font-size:22px;line-height:34px;text-align:center;white-space:nowrap;
}
.partners{position:absolute;left:430px;top:323px;display:flex;gap:36px;align-items:center}
.partner{display:flex;align-items:center;gap:7px;font-family:"Ubuntu",sans-serif;font-weight:500;font-size:18px}
.partner-dot{width:12px;height:12px;border-radius:50%;background:var(--white)}
.contact{position:absolute;left:428px;font-family:"Questrial",sans-serif;font-size:18px;line-height:24px;display:flex;gap:10px}
.contact-address{top:502px}
.contact-web{font-size:17px}
.contact-web.first{top:585px}
.contact-web.second{top:613px}
.icon{flex:none}
</style>
</head>
<body>
<main class="flyer">
  <svg class="flyer-shapes" width="1006" height="670" viewBox="0 0 1006 670" aria-hidden="true">
    <polygon points="300,520 1006,228 1006,582 300,582" fill="var(--brand-blue)"/>
    <polygon points="330,522 1006,244 1006,258 345,522" fill="var(--silver)"/>
    <polygon points="0,422 540,582 0,582" fill="var(--slate)"/>
    <rect x="0" y="582" width="1006" height="63" fill="var(--band-navy)"/>
    <polygon points="40,645 200,582 215,582 55,645" fill="#1a3d78"/>
    <rect x="0" y="645" width="1006" height="25" fill="var(--slate)"/>
  </svg>

  <h1 class="speaker-name">Jonathan Everett Marlow</h1>
  <h2 class="event-title">THE <span class="highlight">GREATEST</span> SALE</h2>
  <p class="event-venue">SILVER RIDGE GOLF CLUB</p>
  <p class="event-date">FRIDAY, AUGUST 9TH, 2019</p>

  <div class="partners">
    <span class="partner"><span class="partner-dot"></span>Signcraft</span>
    <span class="partner"><span class="partner-dot"></span>SRGC</span>
  </div>

  <p class="contact contact-address">
    <svg class="icon" width="20" height="22" viewBox="0 0 20 22"><circle cx="10" cy="9" r="8" fill="none" stroke="#fff" stroke-width="1.6"/><circle cx="10" cy="9" r="3" fill="#fff"/><path d="M5 15 L10 21 L15 15" fill="none" stroke="#fff" stroke-width="1.6"/></svg>
    <span>4200 Harbourview Pkwy,<br>Bayfield, Canada</span>
  </p>
  <p class="contact contact-web first">
    <svg class="icon" width="14" height="23" viewBox="0 0 14 23"><circle cx="7" cy="12" r="6" fill="none" stroke="#fff" stroke-width="1.3"/><circle cx="7" cy="12" r="2.5" fill="#fff"/></svg>
    <span>signcraft.ca</span>
  </p>
  <p class="contact contact-web second">
    <svg class="icon" width="14" height="23" viewBox="0 0 14 23"><circle cx="7" cy="12" r="6" fill="none" stroke="#fff" stroke-width="1.3"/><circle cx="7" cy="12" r="2.5" fill="#fff"/></svg>
    <span>jonathaneverettmarlow.com</span>
  </p>

  <svg class="speaker-photo" width="1006" height="670" viewBox="0 0 1006 670" role="img" aria-label="Headshot of the speaker smiling in a navy suit and white shirt">
    <defs>
      <linearGradient id="photoTone" x1="0" y1="0" x2="0" y2="1">
        <stop offset="0" stop-color="#3a2a24"/>
        <stop offset="0.35" stop-color="#2a2c44"/>
        <stop offset="1" stop-color="#16224a"/>
      </linearGradient>
    </defs>
    <path d="M862,225 Q862,152 925,152 Q990,152 990,225 L990,290 Q1006,300 1006,330 L1006,670 L692,670 L700,560 Q718,440 800,385 L845,335 Q864,322 868,300 Z" fill="url(#photoTone)"/>
  </svg>
</main>
</body>
</html>
```